Minimalist Professional Business Card Design

We will be revamping our marketing materials: Business cards, Website and Catalogs.
Our Overall Design direction is to have a Minimalist artwork with Professionalism and Premium feel. The revamp starts with the new business card design followed by the others. Thus the designer whom work is selected for this job will likely to follow through with the subsequent jobs.

Target Market(s)

Upscale

Industry/Entity Type

Manufacturing

Contact Information for Business Card

For the Business Cards, the following are required:
. Minimalist yet Professional and Premium Feel
. Background Colors: white and / or light pastel yellow and if needed to smoothen the yellow, the light grey can be incorporated. We are changing our corporate bright yellow to either one of the three alternatives:
1. Soylant yellow CMYK (1%, 0%, 52%, 3%)
2. Popcorn yellow CMYK (0%, 0%, 33%, 0%)
3. Papaya yellow CMYK (0%, 0%, 51%, 0%)

Information to be inputed in the business cards:

Name: Ravel Amwerdi
Position: Managing Director

Company's name: Brolvane Valves Pte. Ltd.
Address: 412 Telbrook Lane #07-09K
Singapore 731852
Tel: (65) 6281 9046
Fax: (65) 6287 1149
Email: ravel@brolvanevalves.example
Website: www.brolvanevalves.example
Skype: Brolvane.Valves
Whatsapp/ Line/ Viber/ WeChat: (65) 9827 6013

Company's Logo
Company's Slogan
Two product photos placed side by side (if this gets into the way of the design, it is OK not to include them)

Font styles to use
Serif

Colors
ffffff

Requirements
Must have
• Minimalist
Should not have
• Messy, crowded, playful

```html
<!DOCTYPE html>
<html lang="en">
<head>
<meta charset="utf-8">
<title>Brolvane Valves – Business Card</title>
<link rel="stylesheet" href="https://fonts.googleapis.com/css2?family=Lora:ital,wght@0,400;0,500;0,700;1,500&display=swap">
<style>
  :root {
    --stage: #2a2a2a;
    --pastel: #ffff9e;
    --pastel-soft: #fffbd0;
    --paper: #ffffff;
    --ink: #4a4a4a;
    --ink-soft: #5e5e5e;
    --grey-line: #bdbdbd;
    --band-dark: #5a5a5a;
    --band-mid: #9a9a9a;
    --band-light: #d6d6d6;
    --line-dark: #2a2a2a;
  }
  * { margin: 0; padding: 0; box-sizing: border-box; }
  html, body { width: 1200px; height: 900px; overflow: hidden; background: var(--stage); }
  body { position: relative; font-family: "Lora", Georgia, serif; }

  .card { position: absolute; left: 250px; width: 700px; height: 400px; overflow: hidden; }
  .card-front { top: 30px; background: linear-gradient(115deg, var(--pastel) 0%, var(--pastel-soft) 55%, #f2f2ea 100%); }
  .card-back { top: 470px; background: var(--paper); }

  .brand-mark { position: absolute; left: 305px; top: 45px; width: 90px; height: 90px; border: 6px solid var(--band-dark); border-radius: 50%; }
  .brand-name { position: absolute; left: 0; right: 0; top: 152px; text-align: center; font: 700 54px/1 "Lora", Georgia, serif; letter-spacing: 3px; color: var(--ink); }
  .rule-left { position: absolute; left: 0; top: 232px; width: 130px; height: 4px; background: var(--band-mid); }
  .rule-right { position: absolute; left: 560px; top: 268px; width: 140px; height: 4px; background: var(--line-dark); }
  .slogan { position: absolute; left: 140px; top: 220px; font: italic 500 23px/1.2 "Lora", Georgia, serif; color: var(--ink); transform: rotate(4deg); transform-origin: left center; white-space: nowrap; }

  .identity { position: absolute; right: 310px; top: 112px; text-align: right; color: var(--ink); }
  .person-name { font: 700 24px/1.2 "Lora", Georgia, serif; letter-spacing: .5px; }
  .person-role { font: 500 15px/1.6 "Lora", Georgia, serif; letter-spacing: .5px; }
  .person-email { font: 400 14px/1.5 "Lora", Georgia, serif; }
  .divider { position: absolute; left: 408px; top: 112px; width: 1px; height: 152px; background: var(--grey-line); }

  .contact { position: absolute; left: 428px; top: 110px; color: var(--ink-soft); font: 400 14px/1.5 "Lora", Georgia, serif; list-style: none; }
  .contact .gap { margin-top: 5px; }
  .contact li { display: flex; align-items: center; gap: 8px; }
  .contact svg { width: 13px; height: 13px; flex: none; }
  .dot { width: 12px; height: 12px; border-radius: 50%; background: var(--ink-soft); flex: none; }

  .band-thin { position: absolute; left: 0; top: 290px; width: 700px; height: 14px; background: var(--pastel); }
  .band-web { position: absolute; left: 0; top: 304px; width: 560px; height: 46px; background: var(--band-dark); color: #ffffff; font: 400 18px/46px "Lora", Georgia, serif; letter-spacing: 3px; padding-left: 110px; white-space: nowrap; }
  .band-end { position: absolute; left: 560px; top: 304px; width: 140px; height: 46px; background: var(--band-light); }
  .band-mark { position: absolute; left: 545px; top: 297px; width: 60px; height: 60px; border-radius: 50%; background: var(--pastel); border: 5px solid var(--band-dark); }
</style>
</head>
<body>
  <section class="card card-front" aria-label="Card front">
    <div class="brand-mark"></div>
    <div class="brand-name">BROLVANE</div>
    <div class="rule-left"></div>
    <p class="slogan">Made With Pride For Heavy Duty</p>
    <div class="rule-right"></div>
  </section>

  <section class="card card-back" aria-label="Card back">
    <div class="identity">
      <p class="person-name">RAVEL AMWERDI</p>
      <p class="person-role">MANAGING DIRECTOR</p>
      <p class="person-email">ravel@brolvanevalves.example</p>
    </div>
    <div class="divider"></div>
    <ul class="contact">
      <li>Brolvane Valves Pte. Ltd.</li>
      <li>412 Telbrook Lane #07-09K</li>
      <li>Singapore 731852</li>
      <li class="gap">
        <svg viewBox="0 0 24 24" aria-hidden="true"><path fill="#5e5e5e" d="M6.6 10.8a15.1 15.1 0 0 0 6.6 6.6l2.2-2.2c.3-.3.7-.4 1-.2 1.1.4 2.3.6 3.6.6.6 0 1 .4 1 1V20c0 .6-.4 1-1 1A17 17 0 0 1 3 4c0-.6.4-1 1-1h3.5c.6 0 1 .4 1 1 0 1.3.2 2.5.6 3.6.1.3 0 .7-.2 1z"/></svg>
        (65) 6281 9046
      </li>
      <li>
        <svg viewBox="0 0 24 24" aria-hidden="true"><path fill="#5e5e5e" d="M6 2h10l2 2v5H6zM3 10h18a1 1 0 0 1 1 1v7h-4v4H6v-4H2v-7a1 1 0 0 1 1-1zm5 6v4h8v-4z"/></svg>
        Fax (65) 6287 1149
      </li>
      <li><span class="dot"></span>(65) 9827 6013</li>
      <li><span class="dot"></span>Brolvane.Valves</li>
    </ul>
    <div class="band-thin"></div>
    <div class="band-web">www.brolvanevalves.example</div>
    <div class="band-end"></div>
    <div class="band-mark"></div>
  </section>
</body>
</html>
```